Ecommerce website Home Page Design that is clean and elegant

Design a Home page for an ecommerce website. This website products and offerings will be very similar to :

brightmeadowtrinkets.com
pebblelanegoods.com

Target Market(s)

Consumer and small shops who can order online.

Industry/Entity Type

Retail

Number of Pages Required

1 page

Colors

Designer to choose colors to be used in the design.

Requirements
Must have
• Exact competition with similar products:
• brightmeadowtrinkets.com
• http://www.pebblelanegoods.com/
• Home page with featured image banner
• List of items on sale or category based items list
• atleast three banners for sale or shipping related offers.
Nice to have
• The logo has very light colors and products will have lots of colors as you can see on competition sites. So the design must consider this so that logo also stands out somewhat for branding purpose.
Should not have
• Design should not have black background

```html
<!DOCTYPE html>
<html lang="en">
<head>
<meta charset="utf-8">
<title>Partyvale – Party Supplies &amp; Novelties</title>
<link href="https://fonts.googleapis.com/css2?family=Open+Sans:wght@400;600;700;800&family=Kaushan+Script&family=Playfair+Display:wght@400;700&display=swap" rel="stylesheet">
<style>
:root{
  --pink:#e9637f;
  --pink-soft:#ee8fa5;
  --teal:#5aacb0;
  --purple:#b49ad0;
  --purple-dark:#6b4f8c;
  --yellow:#e8b43f;
  --yellow-btn:#f0b429;
  --charcoal:#3b3b3b;
  --band:#5b5b5b;
  --nav:#e6e6e6;
  --ink:#333333;
  --link:#4a9ea3;
  --rule:#e9e9e9;
  --white:#ffffff;
  --black:#111111;
  --cart-btn:#b8a5cf;
  --foot-text:#d0d0d0;
}
*{box-sizing:border-box;margin:0;padding:0}
html,body{width:1200px;height:3600px;overflow:hidden}
body{font-family:"Open Sans",Arial,sans-serif;color:var(--ink);background:var(--white);position:relative}
.abs{position:absolute}

/* top strip */
.top-strip{left:0;top:0;width:1200px;height:38px;background:var(--pink);color:var(--white);font-size:13px}
.top-strip .welcome{left:77px;top:10px}
.top-strip .call{left:240px;top:10px}
.top-strip .call b{font-weight:700}
.account-links{right:70px;top:4px;display:flex;gap:26px}
.account-links .item{display:flex;align-items:center;gap:6px;font-size:11px;line-height:13px}
.account-links svg{width:20px;height:20px}

/* header */
.site-header{left:0;top:38px;width:1200px;height:627px;background:var(--charcoal)}
.search{left:77px;top:74px;width:283px;height:40px;display:flex}
.search .field{flex:1;background:var(--white);font-size:13px;color:#666;padding:11px 8px}
.search .go{width:40px;background:var(--yellow-btn);color:var(--charcoal);font-weight:700;font-size:14px;display:flex;align-items:center;justify-content:center}
.brand{left:470px;top:62px;width:260px;text-align:center;font-family:"Kaushan Script",cursive;font-size:54px;line-height:64px;color:var(--teal)}
.cart{right:77px;top:82px;display:flex;align-items:center;gap:10px;color:var(--white);font-size:14px}
.cart svg{width:26px;height:22px}

.main-nav{left:77px;top:139px;width:1046px;height:53px;background:var(--nav);display:flex;border-bottom:2px solid #cfcfcf}
.main-nav .nav-item{flex:1;display:flex;align-items:center;justify-content:center;text-align:center;font-size:12.5px;font-weight:700;line-height:15px;color:var(--ink);border-right:1px solid #cdcdcd}
.main-nav .nav-item:last-child{border-right:none}

/* hero */
.hero{left:77px;top:202px;width:1046px;height:463px;background:var(--black);overflow:hidden}
.hero-photo{left:0;top:0;width:560px;height:463px;background:radial-gradient(circle at 50% 35%,#c98a6a 0%,#8a4f3a 35%,#b73b6e 60%,#1a0f12 100%)}
.sale-badge{left:31px;top:38px;width:197px;height:125px;background:#e21f26;color:var(--white);text-align:center;transform:rotate(-4deg);border:3px solid #b5141a}
.sale-badge .t1{font-size:34px;font-weight:800;line-height:34px;margin-top:10px}
.sale-badge .t2{font-size:13px;font-weight:700}
.sale-badge .t3{font-size:22px;font-weight:800;line-height:24px}
.hero-copy{left:542px;top:110px;color:var(--white);font-size:26px}
.btn{display:inline-flex;align-items:center;justify-content:center;font-weight:700;color:var(--white)}
.hero-copy .btn{margin-top:18px;width:132px;height:38px;background:var(--teal);font-size:15px}
.hero-arrow{top:215px;width:28px;height:34px}
.hero-arrow.prev{left:-5px}
.hero-arrow.next{right:20px}
.hero-tabs{left:619px;top:586px;display:flex;gap:7px}
.hero-tab{width:160px;height:67px;background:#d6d6d6;color:var(--ink);padding:10px 12px;font-size:15px;font-weight:700;line-height:18px}
.hero-tab small{display:block;font-size:12px;font-weight:400;color:#555}
.hero-tab.active{background:var(--teal);color:var(--white)}
.hero-tab.active small{color:var(--white)}

/* shipping offers */
.offer-band{left:0;top:672px;width:1200px;height:156px;background:var(--band)}
.offers{left:139px;top:691px;width:924px;height:120px;display:flex}
.offer{flex:1;color:var(--white);text-align:center;padding-top:14px;font-weight:700;font-size:17px;line-height:23px}
.offer.teal{background:var(--teal)}
.offer.purple{background:var(--purple)}
.offer.pink{background:var(--pink-soft)}
.offer .code{display:inline-block;margin-top:8px;background:var(--white);color:var(--ink);font-size:13px;font-weight:600;padding:4px 16px}

/* promo tiles */
.promo-row{left:74px;top:869px;width:1052px;height:254px;display:flex;gap:12px}
.promo{flex:1;position:relative;overflow:hidden}
.promo .title{position:absolute;left:16px;top:10px;color:var(--white);font-size:27px;line-height:29px}
.promo .shop{position:absolute;right:8px;bottom:8px;background:var(--black);color:var(--white);font-size:13px;font-weight:700;padding:6px 14px}
.promo.wedding{background:linear-gradient(135deg,#7a5a42,#c9b7a0 55%,#5c4330)}
.promo.glow{background:radial-gradient(circle at 50% 55%,#2fd3e0 0%,#7be04c 25%,#e0329b 45%,#050505 75%)}
.promo.theme{background:linear-gradient(135deg,#8a1f1f,#d8533a 45%,#3b1414)}

/* section headings */
.section-head{left:74px;width:1052px;height:40px}
.section-head .bar{position:absolute;top:14px;height:16px;background:var(--rule)}
.section-head .bar.l{left:0;width:380px}
.section-head .bar.r{right:0;width:380px}
.section-head h2{position:absolute;left:0;right:0;text-align:center;font-family:"Kaushan Script",cursive;font-weight:400;font-size:27px;color:var(--ink)}

/* categories */
.cat{width:240px;text-align:center}
.cat .pic{width:240px;height:197px}
.cat .name{margin-top:10px;font-size:15px;color:var(--ink)}
.cat .more{font-size:12px;color:var(--link);margin-top:1px}

/* view more */
.view-more{left:74px;width:1052px;height:30px}
.view-more .line{position:absolute;left:0;right:0;top:13px;height:5px;background:#4a4a4a}
.view-more .btn{position:absolute;left:478px;top:0;width:108px;height:30px;background:var(--charcoal);font-size:14px;font-weight:600}

/* wedding banner */
.wedding-banner{left:74px;top:1843px;width:1052px;height:259px;background:linear-gradient(90deg,#8c7b63,#cfc3b0 40%,#d9cfbf 60%,#b9a88e);overflow:hidden}
.wedding-banner .left-photo{left:0;top:0;width:320px;height:259px;background:linear-gradient(135deg,#4f5a3a,#a9a083 55%,#d8d1c0)}
.wedding-banner .right-photo{left:740px;top:0;width:312px;height:259px;background:radial-gradient(circle at 40% 60%,#ffffff 0%,#eee9e2 40%,#c8b9a3 100%)}
.wedding-copy{left:347px;top:10px;width:300px;text-align:center;color:var(--white)}
.wedding-copy .big{font-family:"Playfair Display",serif;font-size:64px;line-height:58px}
.wedding-copy .sub{font-size:24px;line-height:30px;margin-top:10px}
.wedding-copy .upto{font-size:16px;line-height:18px;margin-top:6px}
.wedding-copy .pct{font-size:42px;font-weight:700;line-height:44px}
.wedding-side{left:870px;top:44px;width:130px;text-align:center;color:#6c5a45}
.wedding-side .n{font-size:40px;font-weight:700;line-height:44px}
.wedding-side .s{font-size:16px;line-height:19px}
.wedding-side .btn{margin-top:14px;width:92px;height:30px;background:var(--black);font-size:13px}

/* circles */
.bubble{width:240px;height:240px;border-radius:50%;color:var(--white);text-align:center}
.bubble svg{margin-top:48px;width:64px;height:64px}
.bubble .label{font-size:26px;line-height:30px;margin-top:8px}
.bubble .btn{position:absolute;left:78px;bottom:-8px;width:84px;height:26px;border-radius:10px;font-size:12px}
.bubble.teal{background:var(--teal)}
.bubble.teal .btn{background:#205c5f}
.bubble.purple{background:var(--purple)}
.bubble.purple .btn{background:#3f2d54}
.bubble.pink{background:var(--pink-soft)}
.bubble.pink .btn{background:#4a1f2a}
.bubble.yellow{background:var(--yellow)}
.bubble.yellow .btn{background:#4a3410}

/* products */
.product{width:240px}
.product .pic{width:240px;height:219px}
.product .name{margin-top:20px;font-size:13px;color:var(--link);line-height:17px;height:34px}
.product .price{margin-top:12px;font-size:15px;font-weight:700;color:var(--ink)}
.product .add{margin-top:14px;width:120px;height:26px;background:var(--cart-btn);font-size:12px;font-weight:700}

/* semi-annual */
.sale-banner{left:74px;top:2938px;width:1052px;height:256px;background:var(--pink-soft);overflow:hidden}
.sale-art{left:150px;top:20px;width:520px;height:216px;background:radial-gradient(ellipse at 50% 60%,#f6cb3c 0%,#f6cb3c 22%,#f3a6b8 55%,var(--pink-soft) 75%)}
.stock-blob{left:700px;top:4px;width:330px;height:248px}
.stock-copy{left:740px;top:52px;width:260px;text-align:center;color:var(--white)}
.stock-copy .big{font-size:44px;font-weight:700;line-height:46px}
.stock-copy .s{font-size:16px;line-height:18px;margin-top:6px}
.stock-copy .btn{margin-top:14px;width:110px;height:34px;background:var(--black);font-size:14px}

/* footer */
.site-footer{left:0;top:3235px;width:1200px;height:365px;background:var(--charcoal);color:var(--foot-text)}
.foot-col{top:40px}
.foot-col h3{font-size:13px;font-weight:700;color:var(--white);margin-bottom:6px}
.foot-col li{list-style:none;font-size:12.5px;line-height:25.6px}
.newsletter{left:706px;top:36px;width:420px;height:154px;background:#2b2b2b;padding:14px 16px}
.newsletter h3{font-size:17px;font-weight:700;color:var(--white)}
.newsletter p{font-size:12px;margin-top:4px}
.newsletter .form{display:flex;margin-top:12px;height:34px}
.newsletter .form .field{flex:1;background:var(--white);color:#666;font-size:12px;padding:9px 8px}
.newsletter .form .join{width:68px;background:var(--black);color:var(--white);font-weight:700;font-size:14px;display:flex;align-items:center;justify-content:center}
.social{left:706px;top:204px;width:420px;text-align:center}
.social h4{font-size:13px;font-weight:700;color:var(--white)}
.social .icons{display:flex;justify-content:center;gap:8px;margin-top:10px}
.social .icons span{width:36px;height:36px;border-radius:50%;background:#9a9a9a}
.foot-rule{left:74px;top:281px;width:1052px;height:1px;background:#555}
.copyright{left:74px;top:311px;font-size:12px;color:var(--foot-text)}
.foot-brand{left:470px;top:289px;width:260px;text-align:center;font-family:"Kaushan Script",cursive;font-size:48px;line-height:60px;color:var(--teal)}
.accept{left:770px;top:305px;display:flex;align-items:center;gap:8px;font-size:13px;font-weight:700;color:var(--white)}
.accept .card{width:46px;height:28px;border-radius:3px;background:#e4e4e4}
</style>
</head>
<body>

<div class="abs top-strip">
  <span class="abs welcome">Welcome to Partyvale</span>
  <span class="abs call">Call Us: <b>1-800-000-0000</b></span>
  <div class="abs account-links">
    <div class="item"><svg viewBox="0 0 20 20"><circle cx="10" cy="7" r="4" fill="none" stroke="#fff" stroke-width="1.6"/><path d="M3 18c1-4 4-5 7-5s6 1 7 5" fill="none" stroke="#fff" stroke-width="1.6"/></svg><span>Hello<br>Log in</span></div>
    <div class="item"><svg viewBox="0 0 20 20"><path d="M10 17 3 10a4 4 0 0 1 7-5 4 4 0 0 1 7 5z" fill="none" stroke="#fff" stroke-width="1.6"/></svg><span>Wish<br>List</span></div>
    <div class="item"><svg viewBox="0 0 20 20"><rect x="2" y="6" width="10" height="8" fill="none" stroke="#fff" stroke-width="1.6"/><path d="M12 9h4l2 3v2h-6z" fill="none" stroke="#fff" stroke-width="1.6"/><circle cx="6" cy="16" r="1.6" fill="#fff"/><circle cx="15" cy="16" r="1.6" fill="#fff"/></svg><span>Track<br>Orders</span></div>
  </div>
</div>

<div class="abs site-header"></div>
<div class="abs search"><span class="field">Enter Keyword or Item #</span><span class="go">Go</span></div>
<div class="abs brand">Partyvale</div>
<div class="abs cart">
  <svg viewBox="0 0 26 22"><path d="M1 2h4l3 12h13l3-9H7" fill="none" stroke="#fff" stroke-width="1.8"/><circle cx="10" cy="18" r="2" fill="#fff"/><circle cx="19" cy="18" r="2" fill="#fff"/></svg>
  <span>SHOPPING CART: <b>0</b> Item</span>
</div>

<nav class="abs main-nav">
  <div class="nav-item">Luau</div>
  <div class="nav-item">Party<br>Themes</div>
  <div class="nav-item">Holidays &amp;<br>Occasions</div>
  <div class="nav-item">Decorations &amp;<br>Supplies</div>
  <div class="nav-item">Glow<br>Products</div>
  <div class="nav-item">LED<br>Products</div>
  <div class="nav-item">Party<br>Wearables</div>
  <div class="nav-item">Party<br>Ideas</div>
</nav>

<section class="abs hero">
  <div class="abs hero-photo" role="img" aria-label="Woman wearing a bright tropical flower crown and lei"></div>
  <div class="abs sale-badge"><div class="t1">LUAU<br>SALE</div><div class="t2">UP TO</div><div class="t3">50%OFF</div></div>
  <div class="abs hero-copy">Let's Luau All Summer Long!<br><span class="btn">Shop Now</span></div>
  <svg class="abs hero-arrow prev" viewBox="0 0 28 34"><path d="M20 4 8 17l12 13" fill="none" stroke="#fff" stroke-width="3"/></svg>
  <svg class="abs hero-arrow next" viewBox="0 0 28 34"><path d="M8 4l12 13L8 30" fill="none" stroke="#fff" stroke-width="3"/></svg>
</section>
<div class="abs hero-tabs">
  <div class="hero-tab">SUMMER<small>Shop Now</small></div>
  <div class="hero-tab active">LUAU<small>Shop Now</small></div>
  <div class="hero-tab">WEDDING<small>Shop Now</small></div>
</div>

<div class="abs offer-band"></div>
<div class="abs offers">
  <div class="offer teal">FREE Shipping &amp; $10 Off<br>Orders $99+<br><span class="code">use code:SHIP99</span></div>
  <div class="offer purple">FREE Shipping &amp; $20 Off<br>Orders $199+<br><span class="code">use code:SHIP199</span></div>
  <div class="offer pink">FREE Shipping &amp; $30 Off<br>Orders $299+<br><span class="code">use code:SHIP299</span></div>
</div>

<div class="abs promo-row">
  <div class="promo wedding" role="img" aria-label="Wedding table with lantern, flowers and LOVE letters"><span class="title">Wedding<br>Decorations</span><span class="shop">Shop Now</span></div>
  <div class="promo glow" role="img" aria-label="Tangle of colourful glow necklaces"><span class="title">Glow<br>Necklaces</span><span class="shop">Shop Now</span></div>
  <div class="promo theme" role="img" aria-label="Group of friends in festive holiday hats"><span class="title">Theme<br>Parties</span><span class="shop">Shop Now</span></div>
</div>

<div class="abs section-head" style="top:1156px"><span class="bar l"></span><h2>Shop Top Categories</h2><span class="bar r"></span></div>

<div class="abs cat" style="left:74px;top:1219px"><div class="pic" role="img" aria-label="Colourful party balloons" style="background:radial-gradient(circle at 40% 45%,#e23b3b,#3b6fd6 45%,#f1c232 70%,#f4f4f4)"></div><div class="name">Party &amp; Birthday Balloons</div><div class="more">Shop Now</div></div>
<div class="abs cat" style="left:346px;top:1219px"><div class="pic" role="img" aria-label="Runner wearing a green LED wristband" style="background:radial-gradient(circle at 50% 50%,#6b4c8a,#1a1a1a 60%,#000)"></div><div class="name">LED Jewelry</div><div class="more">Shop Now</div></div>
<div class="abs cat" style="left:614px;top:1219px"><div class="pic" role="img" aria-label="Champagne glasses wrapped in lace fabric" style="background:linear-gradient(135deg,#6d5235,#c8a77a 50%,#7a5a3a)"></div><div class="name">Decorating Fabric</div><div class="more">Shop Now</div></div>
<div class="abs cat" style="left:886px;top:1219px"><div class="pic" role="img" aria-label="Box of pastel anniversary flowers" style="background:radial-gradient(circle at 50% 50%,#e8d4df,#b79bb5 50%,#4e5a48)"></div><div class="name">Anniversary Decorations</div><div class="more">Shop Now</div></div>

<div class="abs cat" style="left:74px;top:1495px"><div class="pic" role="img" aria-label="Table setting with plate and herbs" style="background:radial-gradient(circle at 50% 55%,#efefe8,#8d8a70 55%,#3d3b2c)"></div><div class="name">Tableware</div><div class="more">Shop Now</div></div>
<div class="abs cat" style="left:346px;top:1495px"><div class="pic" role="img" aria-label="Party horn and hats with confetti" style="background:radial-gradient(circle at 50% 45%,#fbe8d4,#f1b89a 55%,#d9604d)"></div><div class="name">Noise Makers</div><div class="more">Shop Now</div></div>
<div class="abs cat" style="left:614px;top:1495px"><div class="pic" role="img" aria-label="Couple posing with photo booth props" style="background:linear-gradient(135deg,#4a7bd1,#e5e5e5 45%,#d84a3a 70%,#2f2f2f)"></div><div class="name">Photo Booth Supplies</div><div class="more">Shop Now</div></div>
<div class="abs cat" style="left:886px;top:1495px"><div class="pic" role="img" aria-label="Row of glowing neon drink cups" style="background:linear-gradient(90deg,#1a1a1a,#2fd36b 25%,#e6d43a 45%,#e0329b 65%,#3a6ff0 85%,#111)"></div><div class="name">Glow Drinkware</div><div class="more">Shop Now</div></div>

<div class="abs view-more" style="top:1773px"><span class="line"></span><span class="btn">View More</span></div>

<section class="abs wedding-banner">
  <div class="abs left-photo" role="img" aria-label="Lantern and white flowers on a rustic wooden table"></div>
  <div class="abs right-photo" role="img" aria-label="Bride and groom cake topper on white roses"></div>
  <div class="abs wedding-copy">
    <div class="big">Wedding<br>Sale</div>
    <div class="sub">Celebrate Your Big Day</div>
    <div class="upto">Up To</div>
    <div class="pct">60% OFF</div>
  </div>
  <div class="abs wedding-side">
    <div class="n">100s</div>
    <div class="s">Of Items - Just<br>Added!</div>
    <span class="btn">Shop Now</span>
  </div>
</section>

<div class="abs bubble teal" style="left:74px;top:2153px">
  <svg viewBox="0 0 64 64"><rect x="12" y="34" width="40" height="20" fill="none" stroke="#fff" stroke-width="3"/><rect x="18" y="22" width="28" height="12" fill="none" stroke="#fff" stroke-width="3"/><path d="M26 14v8M32 12v10M38 14v8" stroke="#fff" stroke-width="3"/></svg>
  <div class="label">Milestone<br>Birthdays</div><span class="btn">Shop Now</span>
</div>
<div class="abs bubble purple" style="left:346px;top:2153px">
  <svg viewBox="0 0 64 64"><circle cx="22" cy="18" r="8" fill="none" stroke="#fff" stroke-width="3"/><circle cx="40" cy="18" r="8" fill="none" stroke="#fff" stroke-width="3"/><rect x="12" y="28" width="34" height="20" fill="none" stroke="#fff" stroke-width="3"/><path d="M46 34l10-6v20l-10-6" fill="none" stroke="#fff" stroke-width="3"/></svg>
  <div class="label">Hollywood<br>Parties</div><span class="btn">Shop Now</span>
</div>
<div class="abs bubble pink" style="left:614px;top:2153px">
  <svg viewBox="0 0 64 64"><rect x="12" y="28" width="40" height="26" fill="none" stroke="#fff" stroke-width="3"/><rect x="8" y="20" width="48" height="8" fill="none" stroke="#fff" stroke-width="3"/><path d="M32 20v34M32 20c-6-10-16-6-10 0M32 20c6-10 16-6 10 0" fill="none" stroke="#fff" stroke-width="3"/></svg>
  <div class="label">Dancefloor<br>Giveaways</div><span class="btn">Shop Now</span>
</div>
<div class="abs bubble yellow" style="left:886px;top:2153px">
  <svg viewBox="0 0 64 64"><path d="M32 4l6 8 10-2 1 10 9 5-5 9 5 9-9 5-1 10-10-2-6 8-6-8-10 2-1-10-9-5 5-9-5-9 9-5 1-10 10 2z" fill="none" stroke="#fff" stroke-width="3"/><text x="32" y="37" text-anchor="middle" font-family="Open Sans,Arial,sans-serif" font-size="12" font-weight="700" fill="#fff">NEW</text></svg>
  <div class="label">New<br>Products</div><span class="btn">Shop Now</span>
</div>

<div class="abs section-head" style="top:2418px"><span class="bar l"></span><h2>Featured Product</h2><span class="bar r"></span></div>

<div class="abs product" style="left:74px;top:2486px"><div class="pic" role="img" aria-label="Green glowing ice cubes in a glass" style="background:radial-gradient(circle at 50% 55%,#7af05a,#1e9a2e 40%,#041004 80%)"></div><div class="name">Neon Green LED and Light - Up Ice Cube - 12 pack</div><div class="price">$22.50</div><span class="btn add">ADD TO CART</span></div>
<div class="abs product" style="left:346px;top:2486px"><div class="pic" role="img" aria-label="Woman wearing a stars and stripes top hat" style="background:radial-gradient(circle at 50% 40%,#d83a3a,#2d4fa8 45%,#111 80%)"></div><div class="name">LED Uncle Sam Hat</div><div class="price">$2.95</div><span class="btn add">ADD TO CART</span></div>
<div class="abs product" style="left:614px;top:2486px"><div class="pic" role="img" aria-label="Person waving a light-up flag foam stick" style="background:radial-gradient(circle at 60% 40%,#e23b3b,#3a5fd0 40%,#0a0a1a 80%)"></div><div class="name">LED American Flag Foam Lumiton</div><div class="price">$2.80</div><span class="btn add">ADD TO CART</span></div>
<div class="abs product" style="left:886px;top:2486px"><div class="pic" role="img" aria-label="Colourful tropical flower lei" style="background:radial-gradient(circle at 50% 50%,#ffffff 0%,#ffffff 25%,#f6c43a 40%,#e8508a 55%,#5aa8e0 70%,#ffffff 85%)"></div><div class="name">Neon Green LED and Light - Up Ice Cube - 12 pack</div><div class="price">$16.00</div><span class="btn add">ADD TO CART</span></div>

<div class="abs view-more" style="top:2864px"><span class="line"></span><span class="btn">View More</span></div>

<section class="abs sale-banner">
  <div class="abs sale-art" role="img" aria-label="Semi-Annual Sale headline lettering on a yellow burst"></div>
  <svg class="abs stock-blob" viewBox="0 0 330 248"><path d="M60 30C110-5 230 0 285 40s50 130 15 170-140 45-200 25S5 180 10 120 20 55 60 30z" fill="var(--purple-dark)"/></svg>
  <div class="abs stock-copy">
    <div class="big">Stock Up!</div>
    <div class="s">ON TOP<br>TRENDING ITEMS</div>
    <span class="btn">Shop Now</span>
  </div>
</section>

<footer class="abs site-footer">
  <div class="abs foot-col" style="left:74px"><h3>CUSTOMER SERVICE</h3><ul><li>Contact Us</li><li>Help &amp; FAQ</li><li>Order Tracking</li><li>Return Policy</li><li>Shipping Information</li><li>Shopping Cart</li><li>International Orders</li></ul></div>
  <div class="abs foot-col" style="left:259px"><h3>ABOUT US</h3><ul><li>Company Information</li><li>Employment</li><li>Affiliate Program</li><li>110% Lowest Price Guarantee</li><li>100% Happiness Guarantee</li><li>Our Family Of Brands</li><li>Company News</li></ul></div>
  <div class="abs foot-col" style="left:494px"><h3>SAFE &amp; SECURE SHOPPING</h3><ul><li>Security/Privacy</li><li>Terms &amp; Conditions</li><li>Your California Privacy Rights</li><li>Site Map</li><li>Safety News</li></ul></div>
  <div class="abs newsletter">
    <h3>JOIN OUR NEWSLETTER</h3>
    <p>Discover exclusive offers, products preview and much more</p>
    <div class="form"><span class="field">Enter your email address</span><span class="join">JOIN</span></div>
  </div>
  <div class="abs social"><h4>STAY CONNECTED WITH PARTYVALE!</h4><div class="icons"><span></span><span></span><span></span><span></span><span></span><span></span></div></div>
  <div class="abs foot-rule"></div>
  <div class="abs copyright">© 2017 Partyvale. All Rights Reserved.</div>
  <div class="abs foot-brand">Partyvale</div>
  <div class="abs accept">WE ACCEPT <span class="card"></span><span class="card"></span><span class="card"></span><span class="card"></span><span class="card"></span></div>
</footer>

</body>
</html>
```